Business card, letterhead, envelope design, email footer for non-profit private equity association
Riviera Growth Capital and Seed Funding Society
Business card, letterhead, envelope design, email footer for non-profit private equity association - Financial Services
Creative Brief
Simple
Tobias Hernquist
Head of Operations
17, Rue des Orangers 98000 Monaco
thernquist@rgsf-example.org
www.rgsf-example.org
Stationery will be prepared for all 7-8 Board Members of our non-profit association. The stationery design is a subsequent process of the new logo design, which has just been created. The Riviera Growth Capital & Seed Funding Society (RGSF) stands for: seriousness and professionalism. Our official website is http://www.rgsf-example.org Please note that this website still includes the OLD logo and layout (to be changed shortly, so please do not let that influence you. This is more to show you the content rather than the design.

```html
<!DOCTYPE html>
<html lang="en">
<head>
<meta charset="utf-8">
<title>RGSF Business Card</title>
<link href="https://fonts.googleapis.com/css2?family=Montserrat:wght@500;700;800&family=Roboto:wght@400;500&display=swap" rel="stylesheet">
<style>
  :root{
    --bg:#d9d9d9;
    --card:#ffffff;
    --ink:#1d1d1d;
    --frame:#0c0c0c;
    --red:#d3202a;
    --grey:#555555;
    --footer-text:#e8e8e8;
  }
  *{box-sizing:border-box;margin:0;padding:0}
  html,body{width:1200px;height:869px;overflow:hidden}
  body{background:var(--bg);font-family:"Roboto",Arial,sans-serif;color:var(--ink);position:relative}

  .card{position:absolute;width:520px;height:300px;border-radius:8px;overflow:hidden;box-shadow:0 10px 24px rgba(0,0,0,.18)}
  .card--back{left:45px;top:284px;background:var(--card);display:flex;flex-direction:column;align-items:center;justify-content:center}
  .card--front{left:635px;top:284px;background:var(--frame);padding:12px}

  .brand{font-family:"Montserrat",Arial,sans-serif;color:var(--ink)}
  .brand__mark{display:flex;align-items:center;gap:12px}
  .brand__square{width:16px;height:16px;background:var(--red)}
  .brand__name{font-weight:800;letter-spacing:4px;line-height:1}
  .brand__full{font-weight:500;text-transform:uppercase;line-height:1.15;letter-spacing:.4px}

  .card--back .brand__name{font-size:64px}
  .card--back .brand__full{font-size:13px;width:300px;margin-top:8px}

  .front__face{position:relative;width:100%;height:100%;background:var(--card);border-radius:4px;overflow:hidden}
  .front__brand{position:absolute;left:22px;top:18px}
  .front__brand .brand__name{font-size:40px}
  .front__brand .brand__square{width:12px;height:12px}
  .front__brand .brand__full{font-size:9px;width:210px;margin-top:5px}

  .contacts{position:absolute;left:22px;top:116px;list-style:none;font-size:9px;color:var(--grey)}
  .contacts li{display:flex;align-items:center;gap:7px;height:15px}
  .contacts svg{width:9px;height:9px;flex:none}

  .person{position:absolute;right:24px;top:150px;text-align:left;width:190px}
  .person__name{font-family:"Montserrat",Arial,sans-serif;font-weight:700;font-size:15px;letter-spacing:1px;text-transform:uppercase}
  .person__role{color:var(--red);font-size:10px;margin-top:2px}
  .person__address{font-size:10px;color:var(--ink);margin-top:12px;line-height:1.4}

  .swoosh{position:absolute;left:0;bottom:0;width:100%;height:110px}
  .front__web{position:absolute;left:40px;bottom:12px;color:var(--footer-text);font-size:11px;letter-spacing:2px}
</style>
</head>
<body>

  <section class="card card--back" aria-label="Business card back">
    <div class="brand">
      <div class="brand__mark">
        <span class="brand__square"></span>
        <span class="brand__name">RGSF</span>
      </div>
      <p class="brand__full">Riviera Growth Capital and Seed Funding Society</p>
    </div>
  </section>

  <section class="card card--front" aria-label="Business card front">
    <div class="front__face">
      <div class="brand front__brand">
        <div class="brand__mark">
          <span class="brand__square"></span>
          <span class="brand__name">RGSF</span>
        </div>
        <p class="brand__full">Riviera Growth Capital and Seed Funding Society</p>
      </div>

      <ul class="contacts">
        <li><svg viewBox="0 0 10 10"><rect width="10" height="10" fill="#d3202a"/></svg>000 555 0142</li>
        <li><svg viewBox="0 0 10 10"><rect width="10" height="10" fill="#d3202a"/></svg>000 555 0143</li>
        <li><svg viewBox="0 0 10 10"><rect width="10" height="10" fill="#d3202a"/></svg>000 555 0144</li>
        <li><svg viewBox="0 0 10 10"><rect width="10" height="10" fill="#d3202a"/></svg>thernquist@rgsf-example.org</li>
      </ul>

      <div class="person">
        <p class="person__name">Tobias Hernquist</p>
        <p class="person__role">Managing Director</p>
        <p class="person__address">17, Rue des Orangers<br>98000 Monaco</p>
      </div>

      <svg class="swoosh" viewBox="0 0 496 110" preserveAspectRatio="none" aria-hidden="true">
        <path d="M0 20 C120 60 230 78 300 82 L0 110 Z" fill="#d3202a"/>
        <path d="M0 34 C140 80 260 92 496 84 L496 110 L0 110 Z" fill="#0c0c0c"/>
      </svg>
      <p class="front__web">www.rgsf-example.org</p>
    </div>
  </section>

</body>
</html>
```